KTR Engineering Business Card Design

We’re looking for an elegant, clean, and timeless business card design that communicates experience, capability, and reliability.

KTR Engineering was established in 1995 , we are a Government Contracting company providing Professional Services to the Ministry of Harbor Works, Frontier Stewardship and the Waypoint Consortium. Our capabilities include: Acquisition & Program Management; Intelligence & Security Operations; Cyber, IT & Network Operations; Lifecycle Logistics & Asset Readiness; C5ISR Systems Engineering & Sustainment.

We want the card to reflect a straightforward, confident approach to business. The design should feel polished and professional without being flashy or overly corporate.

Design Direction
Clean, sophisticated, and uncluttered
Elegant but understated
Strong typography and thoughtful spacing
A timeless aesthetic rather than something overly trendy
Confident and established, with a sense of substance
Easy to read and practical in a real-world business setting

The overall impression should be: “These are experienced professionals who know what they’re doing, do what they say, and can be relied upon.”

We’re open to creative interpretations. The finished card should feel distinctive through its typography, proportions, layout, and attention to detail rather than through excessive graphics or visual effects.

We’re looking for a design that would make a potential client immediately feel that they’re dealing with a capable, trustworthy, and established company.

Company Colors: Navy and Gold/Yellow (but you do not need to use these colors on the card)
Company Name: KTR Engineering Associates, Inc. (known as KTR Engineering)
Website: ktrengineering.example
Company Logo: Navy & Gold (other variations attached)

```html
<!DOCTYPE html>
<html lang="en">
<head>
<meta charset="utf-8">
<title>KTR Engineering – Business Card</title>
<link href="https://fonts.googleapis.com/css2?family=Source+Sans+3:ital,wght@0,400;0,700;0,900;1,400&display=swap" rel="stylesheet">
<style>
  :root {
    --navy: #0d1240;
    --gold: #fde24f;
    --white: #ffffff;
    --backdrop: #e8e8e8;
    --edge: #c9b43a;
  }
  * { margin: 0; padding: 0; box-sizing: border-box; }
  html, body {
    width: 1200px; height: 960px; overflow: hidden;
    background: var(--backdrop);
    font-family: "Source Sans 3", sans-serif;
  }
  .stage { position: relative; width: 1200px; height: 960px; }
  .card {
    position: absolute; width: 756px; height: 432px;
    background: var(--navy); overflow: hidden;
    box-shadow: 0 0 0 1px rgba(0,0,0,0.08);
  }
  .card--front { left: 108px; top: 41px; }
  .card--back { left: 270px; top: 502px; }
  .card__band {
    position: absolute; left: 0; right: 0; bottom: 0; height: 19px;
    background: var(--gold); border-top: 1px solid var(--edge);
  }
  .wordmark {
    position: absolute; color: var(--white);
    font-weight: 900; letter-spacing: -0.3px; line-height: 1; white-space: nowrap;
  }
  .card--front .wordmark { left: 62px; top: 112px; font-size: 38px; }
  .card--back .wordmark { left: 0; right: 0; top: 214px; text-align: center; font-size: 56px; }
  .person { position: absolute; left: 426px; top: 72px; }
  .person__name { color: var(--gold); font-weight: 700; font-size: 32px; line-height: 1.1; }
  .person__title { color: var(--white); font-style: italic; font-size: 20px; line-height: 1.3; }
  .contact {
    position: absolute; left: 426px; top: 232px; list-style: none;
    color: var(--white); font-size: 19.5px; line-height: 24px;
  }
  .contact__item { display: flex; align-items: flex-start; }
  .contact__item--address { margin-bottom: 16px; }
  .contact__icon { width: 36px; flex: none; padding-top: 4px; }
  .contact__icon svg { display: block; }
</style>
</head>
<body>
<main class="stage">

  <section class="card card--front" aria-label="Business card front">
    <div class="wordmark">KTR Engineering</div>

    <div class="person">
      <p class="person__name">Person Name</p>
      <p class="person__title">Director</p>
    </div>

    <ul class="contact">
      <li class="contact__item contact__item--address">
        <span class="contact__icon">
          <svg width="16" height="22" viewBox="0 0 16 22" aria-hidden="true"><path d="M8 0a8 8 0 0 0-8 8c0 6 8 14 8 14s8-8 8-14a8 8 0 0 0-8-8zm0 11a3 3 0 1 1 0-6 3 3 0 0 1 0 6z" fill="var(--gold)"/></svg>
        </span>
        <span>4820 Meridian Street<br>Suite 310, Harbor Point<br>VA 23000</span>
      </li>
      <li class="contact__item">
        <span class="contact__icon">
          <svg width="17" height="17" viewBox="0 0 24 24" aria-hidden="true"><path d="M6.6 10.8a15 15 0 0 0 6.6 6.6l2.2-2.2a1 1 0 0 1 1-.25 11.4 11.4 0 0 0 3.6.57 1 1 0 0 1 1 1V20a1 1 0 0 1-1 1A17 17 0 0 1 3 4a1 1 0 0 1 1-1h3.5a1 1 0 0 1 1 1c0 1.25.2 2.45.57 3.6a1 1 0 0 1-.25 1z" fill="var(--gold)"/></svg>
        </span>
        <span>555-010-4827</span>
      </li>
      <li class="contact__item">
        <span class="contact__icon">
          <svg width="18" height="16" viewBox="0 0 18 16" aria-hidden="true"><path d="M0 6 L9 0 L18 6 V16 H0 Z" fill="var(--gold)"/><path d="M1.5 7 L9 12 L16.5 7" stroke="var(--navy)" stroke-width="1.4" fill="none"/></svg>
        </span>
        <span>info@ktrengineering.example</span>
      </li>
      <li class="contact__item">
        <span class="contact__icon">
          <svg width="17" height="17" viewBox="0 0 20 20" aria-hidden="true"><g fill="none" stroke="var(--gold)" stroke-width="1.5"><circle cx="10" cy="10" r="8.5"/><ellipse cx="10" cy="10" rx="4" ry="8.5"/><path d="M1.5 10h17M3 5.5h14M3 14.5h14M10 1.5v17"/></g></svg>
        </span>
        <span>www.ktrengineering.example</span>
      </li>
    </ul>

    <div class="card__band"></div>
  </section>

  <section class="card card--back" aria-label="Business card back">
    <div class="wordmark">KTR Engineering</div>
    <div class="card__band"></div>
  </section>

</main>
</body>
</html>
```